Thank you for shopping with us business card

We would like a thank you card for our rebranded business. We used to be "Brindle Goods" but are now "Marlow Finds. Old thank you card and new logo will be attached for reference. New thank you card does not have to be same design as old thank you card, but please use new logo.
Shopmart URL is now marlowfinds.shopmart.example
Instagram is @Marlow_Finds
Email is marlowfinds@mailbox.example
Thank you!

Contact Information for Business Card

Shopmart site, email, Instagram

```html
<!DOCTYPE html>
<html lang="en">
<head>
<meta charset="utf-8">
<title>Marlow Finds – Thank You Card</title>
<link rel="stylesheet" href="https://fonts.googleapis.com/css2?family=Montserrat:wght@400;500;700;800&display=swap">
<style>
  :root {
    --backdrop: #3b3b3d;
    --card-blue: #1565ad;
    --card-blue-light: #1c75bf;
    --white: #ffffff;
    --rule: rgba(255, 255, 255, 0.55);
  }
  * { box-sizing: border-box; margin: 0; padding: 0; }
  html, body {
    width: 1200px;
    height: 1200px;
    overflow: hidden;
    background: var(--backdrop);
    font-family: "Montserrat", sans-serif;
  }
  .stage {
    width: 1200px;
    height: 1200px;
    display: flex;
    align-items: center;
    justify-content: center;
  }
  .thank-you-card {
    position: relative;
    width: 1000px;
    height: 690px;
    border-radius: 44px;
    background: linear-gradient(135deg, var(--card-blue) 0%, var(--card-blue-light) 50%, var(--card-blue) 100%);
    color: var(--white);
    overflow: hidden;
  }
  .brand-lockup {
    position: absolute;
    left: 220px;
    top: 100px;
    display: flex;
    align-items: center;
    gap: 34px;
  }
  .brand-square {
    width: 110px;
    height: 110px;
    background: var(--white);
  }
  .brand-divider {
    width: 1px;
    height: 120px;
    background: var(--rule);
  }
  .brand-name {
    font-weight: 700;
    font-size: 46px;
    line-height: 1.05;
    text-transform: uppercase;
    letter-spacing: -0.5px;
  }
  .thanks-band {
    position: absolute;
    left: 0;
    right: 0;
    top: 300px;
    height: 84px;
    background: var(--white);
    display: flex;
    align-items: center;
    padding-left: 200px;
  }
  .thanks-band h1 {
    color: var(--card-blue);
    font-weight: 800;
    font-size: 40px;
    text-transform: uppercase;
    letter-spacing: 0.5px;
  }
  .message {
    position: absolute;
    left: 240px;
    top: 408px;
    font-weight: 500;
    font-size: 34px;
    line-height: 1.25;
    white-space: nowrap;
  }
  .contact-rule {
    position: absolute;
    left: 60px;
    right: 60px;
    top: 582px;
    height: 1px;
    background: var(--rule);
  }
  .contact-row {
    position: absolute;
    left: 60px;
    right: 60px;
    top: 606px;
    display: flex;
    justify-content: space-between;
    list-style: none;
    font-size: 19px;
    font-weight: 500;
  }
  .contact-row li {
    display: flex;
    align-items: center;
    gap: 10px;
  }
  .contact-dot {
    width: 22px;
    height: 22px;
    border-radius: 50%;
    background: var(--white);
    flex: none;
  }
</style>
</head>
<body>
<main class="stage">
  <article class="thank-you-card">
    <div class="brand-lockup">
      <div class="brand-square"></div>
      <div class="brand-divider"></div>
      <div class="brand-name">Marlow<br>Finds</div>
    </div>

    <div class="thanks-band">
      <h1>Thank you for your purchase!</h1>
    </div>

    <p class="message">Your purchase made my day and I<br>hope this package brightens yours.<br>Please come back and leave a review!</p>

    <div class="contact-rule"></div>
    <ul class="contact-row">
      <li><span class="contact-dot"></span>marlowfinds.shopmart.example</li>
      <li><span class="contact-dot"></span>@Marlow_Finds</li>
      <li><span class="contact-dot"></span>marlowfinds@mailbox.example</li>
    </ul>
  </article>
</main>
</body>
</html>
```